Business Card Design

Needing a business card design similar to the business card that is attached.

Industry/Entity Type

Business

Contact Information for Business Card

Design similar to the b-cards that is attached.

```html
<!DOCTYPE html>
<html lang="en">
<head>
<meta charset="utf-8">
<title>Business Cards</title>
<link rel="stylesheet" href="https://fonts.googleapis.com/css2?family=Tinos:wght@400;700&display=swap">
<style>
  :root {
    --backdrop: #e8e3db;
    --card-white: #ffffff;
    --card-black: #141517;
    --card-black-soft: #26282c;
    --accent-red: #d8262f;
    --brand-green: #2f9e3a;
    --brand-teal: #3ab3c9;
    --title-blue: #4d7fc0;
    --divider: #8a8d93;
    --text-light: #eeeeee;
  }
  * { box-sizing: border-box; margin: 0; padding: 0; }
  html, body { width: 1200px; height: 784px; overflow: hidden; }
  body {
    background: var(--backdrop);
    font-family: "Tinos", "Times New Roman", serif;
    position: relative;
  }
  .card {
    position: absolute;
    width: 560px;
    height: 320px;
    background: var(--card-white);
    box-shadow: 0 10px 24px rgba(0,0,0,0.25);
    overflow: hidden;
  }
  .card--energy { left: 60px; top: 60px; }
  .card--realty { left: 580px; top: 404px; }

  .card__brand {
    height: 148px;
    display: flex;
    align-items: center;
    padding-left: 34px;
    gap: 14px;
  }
  .brand-mark { width: 50px; height: 50px; flex: none; }
  .brand-mark--circle { border-radius: 50%; }
  .brand-name {
    font-weight: 700;
    font-size: 38px;
    letter-spacing: -0.5px;
    white-space: nowrap;
  }
  .card--energy .brand-mark { background: var(--brand-green); }
  .card--energy .brand-name { color: var(--brand-green); }
  .card--realty .brand-mark { background: var(--brand-teal); }
  .card--realty .brand-name { color: var(--accent-red); }

  .card__stripe { height: 8px; background: var(--accent-red); }

  .card__info {
    height: 164px;
    background: radial-gradient(ellipse at 40% 30%, var(--card-black-soft), var(--card-black) 75%);
    display: flex;
    align-items: center;
  }
  .person {
    width: 300px;
    text-align: right;
    padding-right: 24px;
  }
  .person__name { color: var(--text-light); font-size: 22px; }
  .person__title { color: var(--title-blue); font-size: 15px; margin-top: 2px; }
  .person__phone { color: var(--accent-red); font-size: 21px; margin-top: 2px; }
  .card__divider {
    width: 1px;
    height: 118px;
    background: var(--divider);
  }
  .contact {
    padding-left: 20px;
    color: var(--text-light);
    font-size: 15px;
    line-height: 1.3;
  }
  .contact__web { color: var(--accent-red); }
  .contact__gap { margin-top: 8px; }
</style>
</head>
<body>

  <section class="card card--energy" aria-label="CedarTherm Energy business card">
    <header class="card__brand">
      <span class="brand-mark brand-mark--circle"></span>
      <span class="brand-name">CedarTherm Energy</span>
    </header>
    <div class="card__stripe"></div>
    <div class="card__info">
      <div class="person">
        <p class="person__name">Daniel Haile</p>
        <p class="person__title">M.E &amp; Certified Geothermal Installer</p>
        <p class="person__phone">(206) 555-0147</p>
      </div>
      <div class="card__divider"></div>
      <div class="contact">
        <p>4820 S 210th St. # B200</p>
        <p>Renton, WA 98055</p>
        <p class="contact__gap">To learn about Geo</p>
        <p>Visit our Website:</p>
        <p class="contact__web">CedarThermEnergy.com</p>
      </div>
    </div>
  </section>

  <section class="card card--realty" aria-label="Harbor Home Group business card">
    <header class="card__brand">
      <span class="brand-mark"></span>
      <span class="brand-name">Harbor Home Group</span>
    </header>
    <div class="card__stripe"></div>
    <div class="card__info">
      <div class="person">
        <p class="person__name">Daniel Haile</p>
        <p class="person__title">Broker</p>
        <p class="person__phone">(206) 555-0147</p>
      </div>
      <div class="card__divider"></div>
      <div class="contact">
        <p>Phone: (206) 555-0147</p>
        <p>Fax: (253) 555-0192</p>
        <p class="contact__web">HarborHomeGroup.com</p>
        <p class="contact__gap">4820 S 210th St. # B200</p>
        <p>Renton, WA 98055</p>
      </div>
    </div>
  </section>

</body>
</html>
```